Presentation card Venture KELO - Tech Incubator from Perú

We need a Design to promote the incubator of technology Startups.
We are in Perú, we work with a string tech filter and develop enterprenurship competencies in the Startup team.
The card is to facilitators and staff memebers of VentureKELO.
We want a clear, modern, tech and agile Design.

We work to help New enterprises of technology here in Perú, we expect the candidates have a big competencies to Research and develop technological products.

We work using methodologies from QRB, Folmestry, Brakewell and Harrowgate univeesities. Our book base is the disciplina of enterpreneur.

We work events all year using diferent formats: Brightforge, Vorne price, OPRA Model Competition you can use these logros in your Design.

Set the name, role, email, cell phone number, address.

Example:
// Contact info section
Tobías Quiroveda
Swift Modeling Hub Manager
tobias.quiroveda@kelo-example.pe
(511) 999 000 417

// Address info section
VentureKELO
Technology-based business incubator
Av. Los Cedrales 884, Valdora
Lima - Perú
web: venture-kelo-example.org.pe
email: venture@kelo-example.pe
phone number: (511) 3926508 ext. 4418

// (optional)Lema section
Making happy using technology

// Social network section
facebook: venturekelooficial

Target Market(s)

Enterprenurship, CTO, Investors, Companies interested on open innovation services

Industry/Entity Type

Information Technology

Contact Information for Business Card

Name, Role, Email, Cell phone number

Colors

Designer to choose colors to be used in the design.

Requirements
Must have
• Logo forms and colors
Nice to have
• I add pictures of the leaders of incubator
Should not have
• No vertical designs

```html
<!DOCTYPE html>
<html lang="en">
<head>
<meta charset="utf-8">
<title>Venture KELO – Business Card</title>
<link href="https://fonts.googleapis.com/css2?family=Roboto:wght@400;500;700&display=swap" rel="stylesheet">
<style>
  :root {
    --magenta: #b8285a;
    --ink: #1d1d1f;
    --paper: #ffffff;
    --stage: #ebe7e2;
    --photo-top: #3a4f6a;
    --photo-mid: #22324a;
    --photo-floor: #b98a5c;
  }
  * { margin: 0; padding: 0; box-sizing: border-box; }
  html, body { width: 1200px; height: 800px; overflow: hidden; }
  body {
    background: var(--stage);
    font-family: "Roboto", Arial, sans-serif;
    position: relative;
  }
  .card {
    position: absolute;
    top: 250px;
    width: 520px;
    height: 300px;
    background: var(--paper);
    box-shadow: 0 6px 18px rgba(0,0,0,0.18);
    overflow: hidden;
  }
  .card--front { left: 50px; }
  .card--back { left: 630px; }

  .card__accent-bar {
    position: absolute;
    left: 0; top: 26px;
    width: 8px; height: 52px;
    background: var(--magenta);
  }
  .card__identity { position: absolute; left: 34px; top: 28px; }
  .card__name {
    font-weight: 700;
    font-size: 17px;
    letter-spacing: 0.5px;
    color: var(--ink);
    text-transform: uppercase;
  }
  .card__role {
    margin-top: 6px;
    font-size: 11.5px;
    line-height: 1.3;
    color: var(--magenta);
    text-transform: uppercase;
    letter-spacing: 0.3px;
  }
  .card__contact {
    position: absolute;
    left: 34px; top: 190px;
    font-size: 11.5px;
    line-height: 1.6;
    color: var(--ink);
  }
  .card__swoosh { position: absolute; left: 0; bottom: 0; width: 520px; height: 300px; }

  .brand {
    position: absolute;
    right: 48px; top: 150px;
    display: flex;
    align-items: center;
    gap: 10px;
  }
  .brand__mark { width: 14px; height: 14px; background: var(--magenta); }
  .brand__name {
    font-weight: 700;
    font-size: 24px;
    line-height: 1;
    color: var(--ink);
    text-transform: uppercase;
    letter-spacing: 0.5px;
  }

  .card__photo {
    position: absolute;
    inset: 10px;
    background: linear-gradient(180deg, var(--photo-top) 0%, var(--photo-mid) 50%, var(--photo-floor) 100%);
  }
</style>
</head>
<body>
  <section class="card card--front" aria-label="Business card front">
    <div class="card__accent-bar"></div>
    <div class="card__identity">
      <h1 class="card__name">Tobías Quiroveda</h1>
      <p class="card__role">Senior Software<br>Development Engineer<br>Peru</p>
    </div>
    <div class="card__contact">
      <p>714.555.0193</p>
      <p>tobiasquiroveda@kelo-example.pe</p>
    </div>
    <div class="brand">
      <span class="brand__mark"></span>
      <span class="brand__name">Venture KELO</span>
    </div>
    <svg class="card__swoosh" viewBox="0 0 520 300" aria-hidden="true">
      <path d="M0,262 C180,280 330,284 410,288 C455,290 495,268 520,236 L520,300 L0,300 Z" fill="var(--magenta)"/>
    </svg>
  </section>

  <section class="card card--back" aria-label="Business card back">
    <div class="card__photo" role="img" aria-label="Group photo of the incubator team in the office"></div>
  </section>
</body>
</html>
```